Step and Repeat Backdrop for wedding reception photo booth

Would like to have a Step and Repeat Backdrop (8 foot high by 10 foot wide) that incorporates the wedding logo (attached) and the names Elena and Gavin. Background should be white, and wedding colors are burgundy and gold. Show me creativity :-) I have included some random samples.

```html
<!DOCTYPE html>
<html lang="en">
<head>
<meta charset="UTF-8">
<title>Elena &amp; Gavin — Step and Repeat Backdrop</title>
<link rel="stylesheet" href="https://fonts.googleapis.com/css2?family=Playfair+Display:wght@400&display=swap">
<style>
  :root {
    --stage: #ececec;
    --backdrop: #ffffff;
    --gold: #b48a2c;
    --gold-light: #d6b35a;
    --gold-deep: #9c7420;
    --shadow: rgba(0, 0, 0, 0.28);
  }
  * { box-sizing: border-box; margin: 0; padding: 0; }
  html, body {
    width: 1200px;
    height: 600px;
    overflow: hidden;
    background: var(--stage);
  }
  .canvas {
    position: relative;
    width: 1200px;
    height: 600px;
    overflow: hidden;
    background: var(--stage);
  }
  .backdrop {
    position: absolute;
    left: 225px;
    top: 0;
    width: 750px;
    height: 600px;
    background: var(--backdrop);
    overflow: hidden;
    box-shadow: 0 0 24px var(--shadow);
  }
  .tile {
    position: absolute;
    width: 76px;
    height: 72px;
    display: flex;
    flex-direction: column;
    align-items: center;
    justify-content: space-between;
  }
  .tile-flourish {
    width: 66px;
    height: 12px;
    border-radius: 6px;
    background: linear-gradient(90deg, rgba(180,138,44,0) 0%, var(--gold) 22%, var(--gold-light) 50%, var(--gold) 78%, rgba(180,138,44,0) 100%);
    opacity: 0.45;
  }
  .tile-mark {
    font-family: "Playfair Display", serif;
    font-weight: 400;
    font-size: 31px;
    line-height: 1;
    color: var(--gold);
    letter-spacing: -1px;
  }
  .emblem {
    position: absolute;
    left: 233px;
    top: 158px;
    width: 285px;
    height: 292px;
    display: flex;
    flex-direction: column;
    align-items: center;
    justify-content: space-between;
  }
  .emblem-flourish {
    width: 282px;
    height: 70px;
    border-radius: 35px;
    background: linear-gradient(90deg, rgba(180,138,44,0) 0%, var(--gold) 20%, var(--gold-light) 50%, var(--gold) 80%, rgba(180,138,44,0) 100%);
    opacity: 0.4;
  }
  .emblem-mark {
    font-family: "Playfair Display", serif;
    font-weight: 400;
    font-size: 118px;
    line-height: 1;
    color: var(--gold-deep);
    letter-spacing: -4px;
  }
</style>
</head>
<body>
<main class="canvas">
  <section class="backdrop" aria-label="Elena and Gavin step and repeat backdrop">

    <div class="tile" style="left:0;top:-22px"><div class="tile-flourish" role="img" aria-label="Gold scroll ornament"></div><span class="tile-mark">E&amp;G</span><div class="tile-flourish" role="img" aria-label="Gold scroll ornament"></div></div>
    <div class="tile" style="left:0;top:74px"><div class="tile-flourish" role="img" aria-label="Gold scroll ornament"></div><span class="tile-mark">E&amp;G</span><div class="tile-flourish" role="img" aria-label="Gold scroll ornament"></div></div>
    <div class="tile" style="left:0;top:199px"><div class="tile-flourish" role="img" aria-label="Gold scroll ornament"></div><span class="tile-mark">E&amp;G</span><div class="tile-flourish" role="img" aria-label="Gold scroll ornament"></div></div>
    <div class="tile" style="left:0;top:324px"><div class="tile-flourish" role="img" aria-label="Gold scroll ornament"></div><span class="tile-mark">E&amp;G</span><div class="tile-flourish" role="img" aria-label="Gold scroll ornament"></div></div>
    <div class="tile" style="left:0;top:449px"><div class="tile-flourish" role="img" aria-label="Gold scroll ornament"></div><span class="tile-mark">E&amp;G</span><div class="tile-flourish" role="img" aria-label="Gold scroll ornament"></div></div>
    <div class="tile" style="left:0;top:556px"><div class="tile-flourish" role="img" aria-label="Gold scroll ornament"></div><span class="tile-mark">E&amp;G</span><div class="tile-flourish" role="img" aria-label="Gold scroll ornament"></div></div>

    <div class="tile" style="left:225px;top:-22px"><div class="tile-flourish" role="img" aria-label="Gold scroll ornament"></div><span class="tile-mark">E&amp;G</span><div class="tile-flourish" role="img" aria-label="Gold scroll ornament"></div></div>
    <div class="tile" style="left:225px;top:74px"><div class="tile-flourish" role="img" aria-label="Gold scroll ornament"></div><span class="tile-mark">E&amp;G</span><div class="tile-flourish" role="img" aria-label="Gold scroll ornament"></div></div>
    <div class="tile" style="left:225px;top:556px"><div class="tile-flourish" role="img" aria-label="Gold scroll ornament"></div><span class="tile-mark">E&amp;G</span><div class="tile-flourish" role="img" aria-label="Gold scroll ornament"></div></div>

    <div class="tile" style="left:450px;top:-22px"><div class="tile-flourish" role="img" aria-label="Gold scroll ornament"></div><span class="tile-mark">E&amp;G</span><div class="tile-flourish" role="img" aria-label="Gold scroll ornament"></div></div>
    <div class="tile" style="left:450px;top:74px"><div class="tile-flourish" role="img" aria-label="Gold scroll ornament"></div><span class="tile-mark">E&amp;G</span><div class="tile-flourish" role="img" aria-label="Gold scroll ornament"></div></div>
    <div class="tile" style="left:450px;top:556px"><div class="tile-flourish" role="img" aria-label="Gold scroll ornament"></div><span class="tile-mark">E&amp;G</span><div class="tile-flourish" role="img" aria-label="Gold scroll ornament"></div></div>

    <div class="tile" style="left:674px;top:-22px"><div class="tile-flourish" role="img" aria-label="Gold scroll ornament"></div><span class="tile-mark">E&amp;G</span><div class="tile-flourish" role="img" aria-label="Gold scroll ornament"></div></div>
    <div class="tile" style="left:674px;top:74px"><div class="tile-flourish" role="img" aria-label="Gold scroll ornament"></div><span class="tile-mark">E&amp;G</span><div class="tile-flourish" role="img" aria-label="Gold scroll ornament"></div></div>
    <div class="tile" style="left:674px;top:199px"><div class="tile-flourish" role="img" aria-label="Gold scroll ornament"></div><span class="tile-mark">E&amp;G</span><div class="tile-flourish" role="img" aria-label="Gold scroll ornament"></div></div>
    <div class="tile" style="left:674px;top:324px"><div class="tile-flourish" role="img" aria-label="Gold scroll ornament"></div><span class="tile-mark">E&amp;G</span><div class="tile-flourish" role="img" aria-label="Gold scroll ornament"></div></div>
    <div class="tile" style="left:674px;top:449px"><div class="tile-flourish" role="img" aria-label="Gold scroll ornament"></div><span class="tile-mark">E&amp;G</span><div class="tile-flourish" role="img" aria-label="Gold scroll ornament"></div></div>
    <div class="tile" style="left:674px;top:556px"><div class="tile-flourish" role="img" aria-label="Gold scroll ornament"></div><span class="tile-mark">E&amp;G</span><div class="tile-flourish" role="img" aria-label="Gold scroll ornament"></div></div>

    <div class="tile" style="left:112px;top:12px"><div class="tile-flourish" role="img" aria-label="Gold scroll ornament"></div><span class="tile-mark">E&amp;G</span><div class="tile-flourish" role="img" aria-label="Gold scroll ornament"></div></div>
    <div class="tile" style="left:112px;top:137px"><div class="tile-flourish" role="img" aria-label="Gold scroll ornament"></div><span class="tile-mark">E&amp;G</span><div class="tile-flourish" role="img" aria-label="Gold scroll ornament"></div></div>
    <div class="tile" style="left:112px;top:262px"><div class="tile-flourish" role="img" aria-label="Gold scroll ornament"></div><span class="tile-mark">E&amp;G</span><div class="tile-flourish" role="img" aria-label="Gold scroll ornament"></div></div>
    <div class="tile" style="left:112px;top:387px"><div class="tile-flourish" role="img" aria-label="Gold scroll ornament"></div><span class="tile-mark">E&amp;G</span><div class="tile-flourish" role="img" aria-label="Gold scroll ornament"></div></div>
    <div class="tile" style="left:112px;top:512px"><div class="tile-flourish" role="img" aria-label="Gold scroll ornament"></div><span class="tile-mark">E&amp;G</span><div class="tile-flourish" role="img" aria-label="Gold scroll ornament"></div></div>

    <div class="tile" style="left:337px;top:12px"><div class="tile-flourish" role="img" aria-label="Gold scroll ornament"></div><span class="tile-mark">E&amp;G</span><div class="tile-flourish" role="img" aria-label="Gold scroll ornament"></div></div>
    <div class="tile" style="left:337px;top:512px"><div class="tile-flourish" role="img" aria-label="Gold scroll ornament"></div><span class="tile-mark">E&amp;G</span><div class="tile-flourish" role="img" aria-label="Gold scroll ornament"></div></div>

    <div class="tile" style="left:562px;top:12px"><div class="tile-flourish" role="img" aria-label="Gold scroll ornament"></div><span class="tile-mark">E&amp;G</span><div class="tile-flourish" role="img" aria-label="Gold scroll ornament"></div></div>
    <div class="tile" style="left:562px;top:137px"><div class="tile-flourish" role="img" aria-label="Gold scroll ornament"></div><span class="tile-mark">E&amp;G</span><div class="tile-flourish" role="img" aria-label="Gold scroll ornament"></div></div>
    <div class="tile" style="left:562px;top:262px"><div class="tile-flourish" role="img" aria-label="Gold scroll ornament"></div><span class="tile-mark">E&amp;G</span><div class="tile-flourish" role="img" aria-label="Gold scroll ornament"></div></div>
    <div class="tile" style="left:562px;top:387px"><div class="tile-flourish" role="img" aria-label="Gold scroll ornament"></div><span class="tile-mark">E&amp;G</span><div class="tile-flourish" role="img" aria-label="Gold scroll ornament"></div></div>
    <div class="tile" style="left:562px;top:512px"><div class="tile-flourish" role="img" aria-label="Gold scroll ornament"></div><span class="tile-mark">E&amp;G</span><div class="tile-flourish" role="img" aria-label="Gold scroll ornament"></div></div>

    <div class="emblem">
      <div class="emblem-flourish" role="img" aria-label="Large gold scroll ornament with fleur-de-lis crest"></div>
      <h1 class="emblem-mark">E&amp;G</h1>
      <div class="emblem-flourish" role="img" aria-label="Large gold scroll ornament with fleur-de-lis point"></div>
    </div>

  </section>
</main>
</body>
</html>
```